Job advertisement

A graphic job advertisement. It's supposed to be slightly different from the normal ads. Eye-catcher and later the text for the job description.

```html
<!DOCTYPE html>
<html lang="de">
<head>
<meta charset="utf-8">
<title>Power-Worker – Stellenanzeige</title>
<link rel="stylesheet" href="https://fonts.googleapis.com/css2?family=Josefin+Sans:wght@600;700&family=Lato:ital,wght@1,900&family=Montserrat:ital,wght@0,700;1,300&display=swap">
<style>
  :root {
    --page-bg: #e8e8e9;
    --poster-top: #3a3560;
    --poster-mid: #26233f;
    --poster-bottom: #1b1a28;
    --glow-purple: rgba(150, 70, 200, 0.55);
    --word-white: #f4f4fa;
    --glitch-cyan: #35d4e6;
    --glitch-pink: #e0407a;
    --badge-pink-light: #f0a8bc;
    --badge-pink: #e95582;
    --badge-shadow: #3b2a44;
  }
  html, body {
    margin: 0;
    width: 1200px;
    height: 1002px;
    overflow: hidden;
    background: var(--page-bg);
  }
  .poster {
    position: absolute;
    left: 258px;
    top: 26px;
    width: 684px;
    height: 950px;
    overflow: hidden;
    background:
      radial-gradient(ellipse 300px 360px at 52% 36%, var(--glow-purple), transparent 70%),
      linear-gradient(180deg, var(--poster-top) 0%, var(--poster-mid) 45%, var(--poster-bottom) 100%);
  }
  .keyword {
    position: absolute;
    margin: 0;
    font-family: "Josefin Sans", sans-serif;
    font-weight: 700;
    letter-spacing: 0.04em;
    color: var(--word-white);
    text-shadow: -2px 1px 0 var(--glitch-cyan), 2px -1px 0 var(--glitch-pink);
    line-height: 1;
  }
  .kw-storm    { left: 52px;  top: 60px;  font-size: 46px; }
  .kw-ampere   { left: 478px; top: 100px; font-size: 36px; }
  .kw-volt     { left: 40px;  top: 208px; font-size: 41px; }
  .kw-ohm      { left: 512px; top: 270px; font-size: 43px; }
  .kw-watt     { left: 49px;  top: 358px; font-size: 47px; }
  .kw-spannung { left: 451px; top: 446px; font-size: 31px; }
  .kw-leistung { left: 52px;  top: 512px; font-size: 32px; }

  .bulb-illustration {
    position: absolute;
    left: 188px;
    top: 80px;
    width: 305px;
    height: 565px;
    border-radius: 150px 150px 60px 60px / 170px 170px 40px 40px;
    background:
      radial-gradient(circle at 48% 34%, #ffd96a 0%, #e08a6a 10%, rgba(170, 90, 200, 0.7) 30%, rgba(110, 70, 170, 0.35) 60%, transparent 80%),
      linear-gradient(180deg, rgba(150, 90, 200, 0.35) 0%, rgba(90, 110, 180, 0.35) 80%, rgba(80, 120, 170, 0.25) 100%);
  }

  .headline {
    position: absolute;
    left: 0;
    right: 0;
    top: 676px;
    margin: 0;
    text-align: center;
    font-family: "Montserrat", sans-serif;
    font-weight: 700;
    font-size: 44px;
    letter-spacing: -0.01em;
    color: var(--word-white);
  }
  .job-badge {
    position: absolute;
    left: 64px;
    top: 744px;
    width: 560px;
    height: 146px;
    box-sizing: border-box;
    border-radius: 12px;
    background: linear-gradient(100deg, var(--badge-pink-light) 0%, var(--badge-pink) 60%, var(--badge-pink) 100%);
    box-shadow: -3px -2px 0 var(--glitch-cyan), 3px 2px 0 #b04bd0;
    text-align: center;
  }
  .job-title {
    margin: 14px 0 0;
    font-family: "Lato", sans-serif;
    font-style: italic;
    font-weight: 900;
    font-size: 76px;
    line-height: 1.05;
    color: #ffffff;
    text-shadow: 4px 4px 0 var(--badge-shadow);
  }
  .job-contact {
    margin: 4px 0 0;
    font-family: "Montserrat", sans-serif;
    font-style: italic;
    font-weight: 300;
    font-size: 19px;
    color: #fff3f6;
  }
</style>
</head>
<body>
  <main class="poster">
    <p class="keyword kw-storm">STORM</p>
    <p class="keyword kw-ampere">AMPERE</p>
    <p class="keyword kw-volt">VOLT</p>
    <p class="keyword kw-ohm">OHM</p>
    <p class="keyword kw-watt">WATT</p>
    <p class="keyword kw-spannung">SPANNUNG</p>
    <p class="keyword kw-leistung">LEISTUNG</p>

    <div class="bulb-illustration" role="img" aria-label="Glühende Glühbirne aus einem Netz von Linien und Punkten in Violett und Blau"></div>

    <h1 class="headline">Wir suchen SIE!</h1>
    <section class="job-badge">
      <h2 class="job-title">Power-Worker</h2>
      <p class="job-contact">Bewerbung an: personal@elektro-lindqvist.de</p>
    </section>
  </main>
</body>
</html>
```